Business Card Design Project

I am opening my own real estate company.

Tarrow & Co. Real Estate Inc.

See attachments for ideas and colors…..
Updates

Project Deadline Extended
Reason: I paid for 5 separate items (graphic design, logo, stationery, brochure & website) all at one time. I thought they all launched at the same time but they did not. That is the reason I have to extend the date.

Target Market(s)

High end real estate properties.

Industry/Entity Type

Real Estate

Font styles to use
Serif
Decorative
Script

Requirements
Must have
• High end design. I want to appeal to very expensive properties.

```html
<!DOCTYPE html>
<html lang="en">
<head>
<meta charset="utf-8">
<title>Tarrow &amp; Co. Real Estate Inc. — Business Card</title>
<link rel="stylesheet" href="https://fonts.googleapis.com/css2?family=Almendra:wght@400&display=swap">
<style>
  :root {
    --backdrop: #2a2928;
    --card-navy: #14123f;
    --card-navy-light: #1f1c55;
    --gold: #d2ad6a;
    --gold-soft: rgba(210, 173, 106, 0.35);
    --card-font: "Almendra", serif;
  }
  html, body {
    margin: 0;
    padding: 0;
    width: 1200px;
    height: 1000px;
    overflow: hidden;
    background: var(--backdrop);
  }
  .canvas {
    position: relative;
    width: 1200px;
    height: 1000px;
    display: flex;
    align-items: center;
    justify-content: center;
  }
  .business-card {
    position: relative;
    width: 900px;
    height: 514px;
    background: var(--card-navy);
    overflow: hidden;
    font-family: var(--card-font);
    color: var(--gold);
  }
  .background-pattern {
    position: absolute;
    inset: 0;
    background:
      radial-gradient(ellipse 340px 260px at 62% 52%, var(--card-navy-light), transparent 70%),
      radial-gradient(ellipse 200px 160px at 90% 20%, var(--card-navy-light), transparent 70%),
      radial-gradient(ellipse 220px 150px at 15% 85%, var(--card-navy-light), transparent 70%);
  }
  .fold-line {
    position: absolute;
    inset: 0;
  }
  .brand {
    position: absolute;
    top: 70px;
    left: 0;
    right: 0;
    text-align: center;
  }
  .brand-dot {
    display: block;
    width: 46px;
    height: 46px;
    margin: 0 auto 70px;
    border-radius: 50%;
    background: var(--gold);
  }
  .brand-name {
    margin: 0;
    font-size: 58px;
    font-weight: 400;
    line-height: 1;
    letter-spacing: 1px;
  }
  .brand-tagline {
    margin: 6px 0 0;
    font-size: 22px;
    font-weight: 400;
    line-height: 1;
  }
  .contact {
    position: absolute;
    right: 40px;
    bottom: 54px;
    margin: 0;
    padding: 0;
    list-style: none;
    font-size: 23px;
    line-height: 1.7;
    text-align: right;
  }
  .contact-label {
    margin-right: 6px;
  }
</style>
</head>
<body>
  <main class="canvas">
    <article class="business-card">
      <div class="background-pattern" role="img" aria-label="Faint tone-on-tone floral leaves and swirls pattern"></div>

      <svg class="fold-line" width="900" height="514" viewBox="0 0 900 514" aria-hidden="true">
        <line x1="0" y1="300" x2="290" y2="300" stroke="var(--gold-soft)" stroke-width="1"/>
        <line x1="610" y1="300" x2="900" y2="300" stroke="var(--gold-soft)" stroke-width="1"/>
      </svg>

      <header class="brand">
        <span class="brand-dot" aria-hidden="true"></span>
        <h1 class="brand-name">Tarrow &amp; Co</h1>
        <p class="brand-tagline">Real Estate Inc.</p>
      </header>

      <ul class="contact">
        <li><span class="contact-label">[E]</span>tarrowandco.com</li>
        <li><span class="contact-label">[P]</span>012 555 0198</li>
      </ul>
    </article>
  </main>
</body>
</html>
```